Business Card Design Project

Hi,
This is a simple contest. The logo for the back of the card is deigned. See attached files. The front of the card must have :

Directors Name: Dorian
Mob:
e-mail:
Postal Address:
Web Page Adress:

It may also add words: "Leaders in Construction Project Management Services"

Target Market(s)

Business & Home owners alike

Industry/Entity Type

Business

Requirements
Must have
• See details above and logo attached
Should not have
• Images other than logo

```html
<!DOCTYPE html>
<html lang="en">
<head>
<meta charset="utf-8">
<title>Keystone Build Group – Business Card</title>
<link rel="stylesheet" href="https://fonts.googleapis.com/css2?family=Oswald:wght@500;600&display=swap">
<style>
  :root {
    --brand-blue: #009edd;
    --card-white: #ffffff;
    --page-bg: #eeeeee;
  }
  * { margin: 0; padding: 0; box-sizing: border-box; }
  html, body {
    width: 1200px;
    height: 1000px;
    overflow: hidden;
    background: var(--page-bg);
  }
  .canvas {
    position: relative;
    width: 1200px;
    height: 1000px;
  }
  .card {
    position: absolute;
    left: 338px;
    width: 524px;
    height: 302px;
    font-family: "Oswald", "Arial Narrow", sans-serif;
  }
  .card--back {
    top: 157px;
    background: var(--brand-blue);
    display: flex;
    align-items: center;
    justify-content: center;
  }
  .card--front {
    top: 541px;
    background: var(--card-white);
    display: flex;
  }
  .brand-panel {
    width: 286px;
    height: 100%;
    background: var(--brand-blue);
    display: flex;
    align-items: center;
    justify-content: center;
  }
  .wordmark {
    display: flex;
    align-items: center;
    gap: 10px;
    color: var(--card-white);
    font-weight: 600;
    letter-spacing: 0.5px;
    line-height: 1;
  }
  .wordmark__square {
    background: var(--card-white);
    flex: none;
  }
  .wordmark--large { font-size: 28px; }
  .wordmark--large .wordmark__square { width: 40px; height: 40px; }
  .wordmark--medium { font-size: 26px; }
  .wordmark--medium .wordmark__square { width: 38px; height: 38px; }
  .details {
    flex: 1;
    padding: 60px 20px 0 0;
    text-align: right;
    color: var(--brand-blue);
    font-weight: 500;
  }
  .tagline {
    font-size: 11px;
    line-height: 14px;
  }
  .person { margin-top: 40px; }
  .person__name {
    font-size: 17px;
    font-weight: 600;
    line-height: 20px;
  }
  .person__role {
    font-size: 11.5px;
    line-height: 16px;
  }
  .contact {
    list-style: none;
    margin-top: 17px;
    font-size: 8.5px;
    line-height: 17px;
  }
</style>
</head>
<body>
  <main class="canvas">
    <section class="card card--back">
      <div class="wordmark wordmark--large">
        <span class="wordmark__square"></span>
        <span class="wordmark__name">KEYSTONE BUILD GROUP</span>
      </div>
    </section>

    <section class="card card--front">
      <div class="brand-panel">
        <div class="wordmark wordmark--medium">
          <span class="wordmark__square"></span>
          <span class="wordmark__name">KEYSTONE</span>
        </div>
      </div>
      <div class="details">
        <p class="tagline">“Leaders in Construction<br>Project Management Services”</p>
        <div class="person">
          <p class="person__name">DORIAN</p>
          <p class="person__role">Director</p>
        </div>
        <ul class="contact">
          <li>(02) 5550 1842</li>
          <li>hello@keystonebuild.com.au</li>
          <li>27 Harbour Lane Marlow NSW 2150</li>
          <li>www.keystonebuild.com.au</li>
        </ul>
      </div>
    </section>
  </main>
</body>
</html>
```